Flyer for Fundraising Marathon Run for a Charity

Hi. I am running the distance of a marathon race to solicit donations for a charitable cause. I need a well designed flyer to help me solicit support from friends and others. The copy for the flyer is attached. There is a significant amount of written text so it will need to be laid out in a way that is easy to read but also mixes well with some good images and design appeal. I am open to creative ideas. I’ve attached a photo of me from the last time I ran this charity marathon run, the area in Delphi where I will be running and the information for the flyer. These photos don't have to be used if there are animation or drawings that might work with creative appeal. Otherwise, I am open to other stock photos or graphics. Feel free to contact me if you have questions. Thank you !

Industry/Entity Type

Charity

Requirements
Must have
• 8.5 X 11 inches in size

```html
<!DOCTYPE html>
<html lang="en">
<head>
<meta charset="utf-8">
<title>A Special Journey – Fundraising Run Flyer</title>
<link rel="stylesheet" href="https://fonts.googleapis.com/css2?family=Raleway:wght@300;400&family=Arvo:ital,wght@0,400;0,700;1,400&family=Roboto+Slab:wght@300..600&display=swap">
<style>
:root{
  --ink:#1c1c1c;
  --title-blue:#2f6fb5;
  --navy:#1f4a8c;
  --band-blue:#24508f;
  --red:#e42a24;
  --red-dark:#b81d18;
  --orange:#f39320;
  --orange-dark:#d27410;
  --green:#6cbd45;
  --green-dark:#4f9a2f;
  --forest:#1d6a37;
  --forest-dark:#114a24;
  --pink:#d4237a;
  --donate-top:#3a86c8;
  --donate-bottom:#1f4a8c;
  --grey-bar:#c4c4c4;
  --slab:"Roboto Slab","Arvo",serif;
}
*{margin:0;padding:0;box-sizing:border-box}
html,body{width:927px;height:1200px;overflow:hidden;background:#fff}
.flyer{position:relative;width:927px;height:1200px;overflow:hidden;font-family:var(--slab);color:var(--ink);
  background:radial-gradient(ellipse at 70% 20%,#ffffff 0%,#eeeeee 60%,#e2e2e2 100%)}
.backdrop{position:absolute;left:0;top:0}
.abs{position:absolute}
.title{left:40px;top:30px;font-family:"Raleway",sans-serif;font-weight:300;font-size:55px;color:var(--title-blue);letter-spacing:.5px}
.subtitle{left:40px;font-family:"Arvo",serif;font-size:22px;color:var(--title-blue);line-height:1}
.subtitle b{font-size:30px;color:var(--navy)}
.sub1{top:104px}.sub2{top:148px}
.runner-art{left:548px;top:28px;width:280px;height:330px;border-radius:14px;
  background:linear-gradient(180deg,#e53935,#fb8c00,#fdd835,#43a047,#1e88e5,#8e24aa);opacity:.7}
.portrait{left:28px;top:196px;width:228px;height:410px;border-radius:6px;
  background:linear-gradient(180deg,#d9b59a 0%,#c9302c 30%,#b7251f 70%,#3e8e4a 100%)}
.intro{left:294px;top:374px;width:622px;color:var(--navy);font-size:14.5px;line-height:1.38;font-weight:300}
.intro .date{font-family:"Arvo",serif;font-style:italic;font-size:18px;margin:4px 0 2px}
.intro .name{font-family:"Arvo",serif;font-size:18px;font-weight:700}
.intro .big{font-family:"Arvo",serif;font-size:18px;font-weight:700}
.intro p{margin-bottom:8px}
.intro .org{font-family:"Arvo",serif;font-size:18px}
.intro em{font-style:italic}
.intro .url{font-family:"Arvo",serif;font-style:italic;font-weight:700;font-size:15px}
.concept{left:0;top:608px;width:927px;height:108px;background:var(--band-blue);color:#fff;
  font-size:15.5px;line-height:1.33;padding:12px 24px 0 36px;font-weight:300}
.ask{left:40px;top:722px;width:520px;text-align:center;font-size:23px;line-height:1.35;font-weight:300}
.ask-sub{left:120px;top:806px;width:240px;text-align:center;font-size:17.5px;font-weight:500;line-height:1.4}
.step{left:0;width:560px;display:flex;color:#fff;font-family:"Arvo",serif;font-weight:700;font-size:14.5px;line-height:1.38}
.step .num{width:32px;flex:none;font-family:"Raleway",sans-serif;font-weight:300;font-size:27px;display:flex;justify-content:center;align-items:flex-start;padding-top:2px}
.step .txt{padding:6px 0 0 8px}
.step small{font-family:var(--slab);font-weight:300;font-size:14px}
.s1{top:892px;height:34px;background:var(--red)}.s1 .num{background:var(--red-dark)}
.s2{top:932px;height:33px;background:var(--orange)}.s2 .num{background:var(--orange-dark)}
.s3{top:972px;height:49px;background:var(--green)}.s3 .num{background:var(--green-dark)}
.s4{top:1032px;height:94px;background:var(--forest)}.s4 .num{background:var(--forest-dark)}
.donate{left:571px;top:768px;width:337px;height:390px;
  background:linear-gradient(180deg,var(--donate-top),var(--donate-bottom));color:#fff}
.donate-head{height:46px;background:var(--pink);border-radius:12px 12px 0 0;font-family:"Arvo",serif;font-weight:700;font-size:21px;text-align:center;padding-top:10px}
.donate-body{padding:10px 12px 0 18px;font-size:15px;line-height:1.33}
.donate-body p{margin-bottom:14px}
.donate-body .lg{font-size:19px}
.donate-body .payee{font-size:19px;display:block;padding-left:14px;margin:2px 0 10px;line-height:1.25}
.donate-body .payee span{font-size:15px}
.donate-body .ind{padding-left:14px}
.donate-body .addr{padding-left:93px;margin:4px 0 14px;font-size:14.5px}
.footer{left:0;top:1158px;width:927px;height:42px;background:var(--grey-bar);text-align:right;padding:11px 22px 0 0;font-size:16px;font-weight:300}
</style>
</head>
<body>
<div class="flyer">
  <svg class="backdrop" width="927" height="1200" viewBox="0 0 927 1200" aria-hidden="true">
    <defs>
      <linearGradient id="sky" x1="0" y1="0" x2="0" y2="1">
        <stop offset="0" stop-color="#d8f0fb"/><stop offset="1" stop-color="#6cc4ec"/>
      </linearGradient>
      <linearGradient id="mist" x1="0" y1="0" x2="0" y2="1">
        <stop offset="0" stop-color="#9a9a9a"/><stop offset=".35" stop-color="#e6e6e6"/><stop offset="1" stop-color="#f4f4f4"/>
      </linearGradient>
    </defs>
    <g fill="none" stroke-width="22">
      <path d="M-10 265 C80 215 200 205 330 250" stroke="#e53a2c"/>
      <path d="M-10 287 C80 237 200 227 330 272" stroke="#f28a22"/>
      <path d="M-10 309 C80 259 200 249 330 294" stroke="#fbd530"/>
      <path d="M-10 331 C80 281 200 271 330 316" stroke="#7cc34a"/>
    </g>
    <path d="M0 330 C120 262 300 268 430 330 C560 392 680 420 780 385 C850 360 900 305 927 262 L927 608 L0 608 Z" fill="url(#sky)"/>
    <g fill="none" stroke-width="9">
      <path d="M540 378 C640 418 760 412 927 262" stroke="#f06ab0"/>
      <path d="M560 386 C660 424 780 418 927 278" stroke="#d4237a"/>
      <path d="M580 394 C680 430 800 424 927 294" stroke="#8e3fa8"/>
      <path d="M600 402 C700 436 820 430 927 310" stroke="#3c5fb8"/>
    </g>
    <path d="M0 716 L748 716 C650 762 560 866 300 868 C150 868 50 830 0 800 Z" fill="url(#mist)"/>
    <path d="M0 800 C50 830 150 868 300 868 C560 866 650 762 748 716" fill="none" stroke="#8a8a8a" stroke-width="2"/>
  </svg>

  <h1 class="abs title">A Special Journey</h1>
  <div class="abs subtitle sub1">For <b>Your Specific Prayers</b> &amp;</div>
  <div class="abs subtitle sub2">For <b>An Important Ancient Cause</b></div>

  <div class="abs runner-art" role="img" aria-label="Runner silhouette made of rainbow-coloured horizontal stripes"></div>
  <div class="abs portrait" role="img" aria-label="Photo of the runner in a red outfit adorned with colourful prayer cloth strips"></div>

  <div class="abs intro">
    <p style="margin:0">This coming</p>
    <p class="date">April 22 2017,</p>
    <p><span class="name">Daniel Marlowe</span> will make a special running journey of <span class="big">26 miles</span> through the ancient lands of Apollo and Athena at Delphi on Mt. Parnassus in Greece.</p>
    <p>Daniel will adorn his running outfit with special cloth strips that will contain written prayers and petitions of people who will sponsor his journey by making a charitable donation to the <span class="org">Hellenic Heritage Circle</span><em>, an organization that preserves the land and the Delphic culture.</em><br><span class="url">www.hellenic-heritage-circle.org</span></p>
  </div>

  <div class="abs concept">The concept is simple and very powerful: as Daniel runs, your written prayer on a cloth strip will flow and emanate in the wind --- being blessed by the spirits of this ancient and magical land --- asking unto the wind that your prayer be answered.&nbsp; This type of prayer practice dates back to ancient times.&nbsp; The Tibetan culture commonly uses prayer flags with special mantras and symbols.</div>

  <div class="abs ask">Will you make a prayer for yourself or<br>a loved and support a good cause?</div>
  <div class="abs ask-sub">Here is how to get your prayer started:</div>

  <div class="abs step s1"><span class="num">1</span><span class="txt">Decide what you want your prayer, petition or intention to be.</span></div>
  <div class="abs step s2"><span class="num">2</span><span class="txt">Define your prayer, petition or intention by writing it down.</span></div>
  <div class="abs step s3"><span class="num">3</span><span class="txt">Refine it is concise, clear &amp; specific.<br><small>(18 words or less is ideal for each strip cloth).</small></span></div>
  <div class="abs step s4"><span class="num">4</span><span class="txt">Contact Daniel at dmarlowe@marlowegrant.com and tell him how many prayer cloth strips you wish to obtain. Daniel will then send you the cloth for you to write your prayer and send back to him or he will write out the prayer for you.</span></div>

  <div class="abs donate">
    <div class="donate-head">How you can Donate?</div>
    <div class="donate-body">
      <p>A minimum donation of <span class="lg">$25</span> for each prayer cloth is requested.</p>
      <div>1. Checks can be made to the</div>
      <span class="payee">“Daniel Marlowe/Hellenic<br>Heritage Circle” <span>and</span></span>
      <div class="ind">mail to <span class="lg">Daniel R. Marlowe,</span></div>
      <div class="addr">Marlowe Grant PLC,<br>1480 Harbor Lane,<br>Ste. 204 Fairview,<br>Oregon 97024</div>
      <div>2. or though <span class="lg">Givlyn</span> instructions</div>
      <div class="ind">sent by email from Daniel<br>as requested.</div>
    </div>
  </div>

  <div class="abs footer">For more details contact Daniel. He will answer any questions you may have.</div>
</div>
</body>
</html>
```